TallFern's Bold New Thank You Greeting Card 2.0

We want an updated thank you card design that is creative and clever. Same dimensions as the TF_ThankYouCard uploaded below: a half-fold card that fits in a 4 3/8 x 5 3/4" envelope. Looking for design styles that are minimalist, with themes that are bold and playful. Attached files show past designs we have used, but we are looking for something more memorable, while maintaining the same color scheme and fundamental elements of our logo. Additional design examples for reference here: https://www.pinboardly.example/iamdanaprewitt/logo-inspiration/
Updates

Based on the designs I've received so far, I realized I was not clear enough in my original brief. I want it to be a THANK YOU CARD first and foremost, and promotion of our company should appear as secondary afterthought. The front should either say "thank you", or could have a completely unique design without text, but must be WITHOUT our name and logo. I don't want the reader to know who it is from until they open it. There could be hints of who it is from, by incorporating our colors, fonts or the bird element, but our logo should be on the inside or back only. I want a design that includes front, inside and back, but initial submissions can focus on the front design if that's easier. Most of the designs submitted don't follow all the parameters of the brief, so if you go back and read the brief carefully, it should be easy to stand out and win!

Project Deadline Extended
Reason: Because I had to clarify project details and remind designers to read my brief carefully, I believe a few more days will bring a better variety of high quality designs closely aligned with what I'm looking for.

Target Market(s)

Our clients and potential clients. Local Portland OR market. Hipsters, professionals, multi-generational.

Industry/Entity Type

Real Estate

Font styles to use
Sans Serif

Colors
0292cd
ffffff
1b1b1b

Requirements
Must have
• Clever, memorable design that stands out.
• We want to REINVENT our current thank you card. (Attached) I want it to be a THANK YOU CARD first and foremost, and promotion of our company should appear as secondary afterthought.
• The front should either say "thank you", or could have a completely unique design without text, but must be WITHOUT our name and logo. I don't want the reader to know who it is from until they open it. There could be hints of who it is from, by incorporating our colors, fonts or the bird element, but our logo should be on the inside or back only.
• For more info on our companies, go here: http://mytallfern.example
• Also see style guide in attached files.
Nice to have
• Could have a completely different style than the designs I uploaded, but must tie into some elements of our logo. You could add colors as long as they play well with our existing palette. You can break up any elements of our logo and text that you want to create your design.
• Doesn't have to, but any reflection or incorporation of our Core Values (below) would be a bonus:
• TALLFERNS ARE:
• Leaders – We bravely seize opportunity and dare to do things differently.
• Listeners – We practice agenda-free listening.
• Creators – We solve instead of sell.
• Educators – We teach and empower openly and honestly.
• Givers – We exceed expectations and deliver with generosity.
Should not have
• Should not be so silly or playful that it comes across as insincere or irreverent. Don't submit business card designs. I'm only interested in unique and original artwork. Don't just submit a design with our logo and a border on a card.

```html
<!DOCTYPE html>
<html lang="en">
<head>
<meta charset="utf-8">
<title>TallFern Thank You Card</title>
<link href="https://fonts.googleapis.com/css2?family=Montserrat:wght@400;700&family=Nothing+You+Could+Do&display=swap" rel="stylesheet">
<style>
  :root {
    --brand-blue: #0292cd;
    --paper: #ffffff;
    --ink: #1b1b1b;
    --backdrop: #ececec;
    --art-light: rgba(255, 255, 255, 0.55);
    --art-fade: rgba(255, 255, 255, 0.12);
  }
  html, body {
    margin: 0;
    padding: 0;
    width: 1200px;
    height: 1007px;
    overflow: hidden;
    background: var(--backdrop);
  }
  .card {
    position: absolute;
    left: 352px;
    top: 95px;
    width: 496px;
    height: 760px;
    background: var(--paper);
  }
  .card-back {
    position: absolute;
    inset: 0 0 380px 0;
    background: var(--paper);
  }
  .brand-strip {
    position: absolute;
    left: 126px;
    top: 22px;
    width: 342px;
    height: 34px;
    transform: rotate(180deg);
    display: flex;
    align-items: center;
    gap: 12px;
    color: var(--brand-blue);
    font-family: "Montserrat", sans-serif;
  }
  .brand-mark {
    width: 28px;
    height: 28px;
    background: var(--brand-blue);
    flex: none;
  }
  .brand-name {
    font-size: 25px;
    font-weight: 400;
    letter-spacing: -0.5px;
    line-height: 1;
  }
  .brand-divider {
    width: 2px;
    height: 32px;
    background: var(--brand-blue);
    margin: 0 6px;
  }
  .brand-contact {
    display: flex;
    flex-direction: column;
    font-size: 12.5px;
    font-weight: 700;
    line-height: 1.25;
    white-space: nowrap;
  }
  .brand-contact .phone { font-weight: 400; }
  .card-front {
    position: absolute;
    left: 0;
    right: 0;
    bottom: 0;
    height: 380px;
    background: var(--brand-blue);
  }
  .greeting {
    position: absolute;
    left: 260px;
    top: 88px;
    margin: 0;
    color: var(--paper);
    font-family: "Nothing You Could Do", cursive;
    font-weight: 400;
    font-size: 33px;
    line-height: 1;
    white-space: nowrap;
    transform: scaleY(1.3);
    transform-origin: left bottom;
  }
  .bird-family-art {
    position: absolute;
    left: 48px;
    bottom: 0;
    width: 146px;
    height: 79px;
    border-radius: 40px 40px 0 0;
    background: radial-gradient(ellipse at 35% 60%, var(--art-light), var(--art-fade) 75%, transparent);
  }
</style>
</head>
<body>
  <main class="card">
    <section class="card-back">
      <div class="brand-strip">
        <span class="brand-mark"></span>
        <span class="brand-name">tallfern</span>
        <span class="brand-divider"></span>
        <span class="brand-contact">
          <span class="url">www.mytallfern.example</span>
          <span class="phone">503.555.0182</span>
        </span>
      </div>
    </section>
    <section class="card-front">
      <h1 class="greeting">thank you</h1>
      <div class="bird-family-art" role="img" aria-label="White illustration of three small birds of decreasing size standing on thin legs"></div>
    </section>
  </main>
</body>
</html>
```